Website for Youth Orchestra to sell tickets and attract young musicians

We are looking for a new website design for a Youth Orchestra; one of the best classical youth orchestras in the county. This project is the design only. <br/><br/>The website serves two main purposes:<br/>• Selling tickets for concerts and performances of the orchestra<br/>• Recruiting young musicians to do audition for the orchestra<br/>
Updates

Target Market(s)

Classical music lovers with a special interest in young upcoming musicians.
Young talented musicians

Number of Pages Required

2 page

Colors
ec1f27

Requirements
Must have
• - A Picture on the front page that promotes the main upcomming event
• - Attention for recruiting new musicians
• - Pictures with young musicians (white back ground, see examples)
• - Responsive
• - Please use the logo attached
Should not have
• The brown colors of the current website (kvb-veldhorst.example)

```html
<!DOCTYPE html>
<html lang="en">
<head>
<meta charset="utf-8">
<title>Eemstad Jeugdorkest</title>
<link rel="stylesheet" href="https://fonts.googleapis.com/css2?family=Comfortaa:wght@400;700&display=swap">
<style>
  :root {
    --orange: #ef7b21;
    --red: #e8363f;
    --brand: #ec1f27;
    --white: #ffffff;
  }
  * { margin: 0; padding: 0; box-sizing: border-box; }
  html, body { width: 1200px; height: 675px; overflow: hidden; }
  body {
    position: relative;
    background: var(--orange);
    font-family: "Comfortaa", sans-serif;
    color: var(--white);
  }
  .side-band {
    position: absolute; left: 0; top: 0; width: 200px; height: 675px;
    background: var(--red);
  }
  .brand {
    position: absolute; left: 219px; top: 22px;
    display: flex; align-items: center; gap: 6px;
    font-size: 14px; font-weight: 700; line-height: 1.15; width: 115px;
  }
  .brand-dot { width: 8px; height: 8px; border-radius: 50%; background: var(--white); flex: none; }
  .main-nav {
    position: absolute; top: 38px; left: 352px; width: 824px;
    display: flex; justify-content: space-between;
    font-size: 13px; letter-spacing: 0.3px; white-space: nowrap;
  }
  .main-nav a { color: var(--white); text-decoration: none; }
  .main-nav a.active { border-bottom: 1.5px solid var(--white); padding-bottom: 3px; }
  .headline {
    position: absolute; top: 134px; left: 200px; width: 1000px; text-align: center;
    font-size: 30px; font-weight: 400; letter-spacing: 1px; white-space: nowrap;
  }
  .hero-figure {
    position: absolute; left: 112px; top: 240px; width: 513px; height: 435px;
    background:
      radial-gradient(ellipse 30% 28% at 48% 35%, rgba(238,226,210,0.95) 0%, rgba(220,196,170,0.7) 55%, rgba(220,196,170,0) 100%),
      radial-gradient(ellipse 45% 55% at 50% 85%, rgba(45,32,34,0.85) 0%, rgba(70,45,40,0.5) 60%, rgba(70,45,40,0) 100%),
      radial-gradient(ellipse 50% 50% at 50% 55%, rgba(200,150,120,0.35) 0%, rgba(239,123,33,0) 100%);
  }
  .pitch {
    position: absolute; left: 634px; top: 248px; width: 540px; text-align: center;
    font-size: 12.5px; line-height: 15px; letter-spacing: 0.3px;
  }
  .pitch a { color: var(--brand); text-decoration: underline; }
  .promo-photo {
    position: absolute; left: 728px; top: 304px; width: 353px; height: 238px;
    border-radius: 8px; border: 1.5px solid #f4a46a;
    background:
      radial-gradient(ellipse 22% 40% at 55% 35%, rgba(222,190,140,0.85) 0%, rgba(222,190,140,0) 100%),
      #1f2022;
  }
  .btn {
    position: absolute; top: 569px; width: 144px; height: 34px;
    display: flex; align-items: center; justify-content: center;
    font-size: 14px; font-weight: 700; letter-spacing: 0.6px; border-radius: 3px;
    color: var(--white); text-decoration: none;
  }
  .btn-apply { left: 752px; background: var(--brand); }
  .btn-info { left: 914px; border: 2px solid var(--brand); }
  .tagline {
    position: absolute; top: 620px; left: 634px; width: 540px; text-align: center;
    font-size: 12.5px; letter-spacing: 0.3px; white-space: nowrap;
  }
  .slider-arrow {
    position: absolute; top: 594px; width: 62px; height: 62px;
    border: 2px solid var(--white);
  }
  .slider-arrow.prev { left: 125px; }
  .slider-arrow.next { left: 212px; opacity: 0.45; }
  .slider-arrow svg { width: 100%; height: 100%; }
</style>
</head>
<body>
  <div class="side-band"></div>

  <div class="brand"><span class="brand-dot"></span><span>Eemstad Jeugdorkest</span></div>

  <nav class="main-nav">
    <a class="active" href="#">Home</a>
    <a href="#">Orkest</a>
    <a href="#">Speel Mee</a>
    <a href="#">Concerten</a>
    <a href="#">Tournees</a>
    <a href="#">Partners</a>
    <a href="#">Vrienden</a>
    <a href="#">Oudleden</a>
    <a href="#">Contact &amp; Organisatie</a>
  </nav>

  <h1 class="headline">The biggest orchestra of Nederland is recruting!</h1>

  <div class="hero-figure" role="img" aria-label="Violinist playing with closed eyes, cut out against the orange background"></div>

  <p class="pitch">This could be the biggest opportunity of a lifetime. Don't let this moment slip out of your fingers, <a href="#">Apply Now</a> and see what you are capable of!</p>

  <div class="promo-photo" role="img" aria-label="Musician in black holding a bow and pointing toward the viewer, on a dark background"></div>

  <a class="btn btn-apply" href="#">Apply Now</a>
  <a class="btn btn-info" href="#">More Info</a>

  <p class="tagline">Are you one who always wanted to become a famous musician or singer?</p>

  <a class="slider-arrow prev" href="#" aria-label="Previous">
    <svg viewBox="0 0 62 62"><polyline points="40,10 19,31 40,52" fill="none" stroke="#fff" stroke-width="2"/></svg>
  </a>
  <a class="slider-arrow next" href="#" aria-label="Next">
    <svg viewBox="0 0 62 62"><polyline points="22,10 43,31 22,52" fill="none" stroke="#fff" stroke-width="2"/></svg>
  </a>
</body>
</html>
```